Australian Real Estate Sales Consultant needs web design please.

I am a female residential real estate sales consultant for a large australian real estate franchise.
I need a web design for "wordpress" that contains an area that will accommodate my photo and details and company logo.
A large area that contains a feature property where images are on something like a slide show.
Tabs or something similar with images for Selling, Sold, Photography and News where people can look at listings but I do not want people to be able to post a comment.
Reason: Need more designers, may be forced to change to wordpress and offer more money.
Reason: Sorry for the delay, I have been concentrating on another project which I needed completed. I am now able to focus on my web design project and hope to have it all set up in the next 10 days as it is a high priority for me. Thank you for your patience and I will begin providing feedback to your designs shortly. Thanks, Marisha.
Target Market(s)
Potential sellers or purchasers of residential property
Industry/Entity Type
Residential
Requirements
Must have
- Ease of changing property photos and info
Nice to have
- Bright attractive colours

```html
<!DOCTYPE html>
<html lang="en">
<head>
<meta charset="utf-8">
<title>Harbourline Realty – Home</title>
<link href="https://fonts.googleapis.com/css2?family=PT+Sans:wght@400;700&family=Arimo:wght@400;700&display=swap" rel="stylesheet">
<style>
:root{
  --header-grey:#d6d6d6;
  --page-grey:#ebebeb;
  --nav-red:#e8140c;
  --nav-red-dark:#b50c06;
  --nav-blue:#1c1ca8;
  --purple:#7b3fc4;
  --purple-dark:#5a2aa0;
  --ink:#1a1a1a;
  --body-text:#2a2a2a;
  --date-blue:#1a1a8c;
  --white:#ffffff;
  --frame:#cfcfcf;
}
*{margin:0;padding:0;box-sizing:border-box}
html,body{width:1200px;height:1126px;overflow:hidden}
body{position:relative;background:var(--page-grey);font-family:"Arimo",Arial,sans-serif;color:var(--body-text)}
.abs{position:absolute}
.site-header{left:0;top:0;width:1200px;height:141px;background:linear-gradient(#dcdcdc,#cfcfcf)}
.brand{left:175px;top:44px;height:57px;display:flex;align-items:center;gap:12px}
.brand-mark{width:40px;height:40px;background:var(--nav-blue)}
.brand-name{font-family:"PT Sans",sans-serif;font-weight:700;font-size:34px;color:var(--nav-blue)}
.phone{left:831px;top:46px;display:flex;align-items:center;gap:12px}
.phone-icon{width:54px;height:54px;border-radius:50%;background:radial-gradient(circle at 50% 35%,#f4f4f4,#bdbdbd);box-shadow:0 6px 8px rgba(0,0,0,.2);display:flex;align-items:center;justify-content:center}
.phone-number{font-family:"PT Sans",sans-serif;font-size:26px;color:var(--ink)}
.main-nav{left:0;top:142px;width:1200px;height:34px;background:linear-gradient(var(--nav-red),var(--nav-red-dark));border-top:1px solid #900;border-bottom:1px solid #900}
.nav-list{position:absolute;left:174px;top:0;display:flex;list-style:none;height:33px}
.nav-list li{font-family:"PT Sans",sans-serif;font-size:16px;color:var(--white);padding:0 18px;line-height:33px;border-right:1px solid rgba(0,0,0,.25)}
.nav-list li.active{background:var(--nav-blue);padding:0 14px}
.search{position:absolute;left:811px;top:9px;width:217px;height:17px;background:#f2f2f2;border:1px solid #999;font-size:11px;color:#888;padding-left:5px;line-height:15px}
.search svg{position:absolute;right:2px;top:0}
.feature-band{left:0;top:180px;width:1200px;height:438px;background:radial-gradient(ellipse at 50% 40%,#a262ea,var(--purple) 55%,var(--purple-dark))}
.slide-frame{left:174px;top:206px;width:855px;height:387px;background:var(--white);padding:4px;border-radius:3px}
.slide-photo{width:100%;height:100%;background:linear-gradient(180deg,#9ec4e6 0%,#c9b79c 45%,#8a7a66 70%,#7fa04f 100%)}
.slide-arrow{top:380px;color:var(--white);font-size:52px;font-family:"PT Sans",sans-serif;font-weight:700;line-height:40px}
.captions{left:174px;top:596px;width:855px;display:flex;justify-content:space-between;font-family:"PT Sans",sans-serif;font-size:15px;color:var(--white)}
.captions span.sep{opacity:.9}
h2{font-family:"PT Sans",sans-serif;font-weight:400;color:var(--ink)}
.about-title{left:172px;top:630px;font-size:26px}
.about-text{left:174px;top:669px;width:402px;font-size:11px;line-height:16px;text-align:justify}
.about-text p{margin-bottom:16px}
.about-more{left:174px;top:849px;width:582px;font-size:11px;line-height:16px;text-align:justify}
.agent-photo{left:591px;top:632px;width:171px;height:204px;background:var(--white);border:1px solid var(--frame);padding:3px}
.agent-photo div{width:100%;height:100%;background:linear-gradient(#e6e3df,#bdb6ae 55%,#2b2b2b 80%)}
.props-title{left:173px;top:916px;font-size:26px}
.props-box{left:175px;top:954px;width:585px;height:112px;background:#f4f4f4;border:1px solid #ddd;border-radius:4px}
.prop-thumb{top:969px;width:117px;height:82px;border:2px solid var(--white);box-shadow:0 0 2px #999}
.prop-arrow{top:992px}
.news-title{left:779px;top:624px;font-size:26px}
.news-item{left:779px;width:249px;height:97px;border-bottom:1px solid #ddd}
.news-thumb{position:absolute;left:0;top:0;width:76px;height:76px;background:var(--white);border:1px solid var(--frame);padding:3px}
.news-thumb div{width:100%;height:100%}
.news-body{position:absolute;left:84px;top:0;width:165px;font-size:10.5px;line-height:13px}
.news-date{color:var(--date-blue);font-weight:700}
.read-more{position:absolute;right:14px;top:62px;font-size:11px;font-weight:700;text-decoration:underline;color:var(--ink)}
.testimonial{left:779px;top:877px;width:249px;height:190px;background:linear-gradient(#fafafa,#e4e4e4);border:1px solid #ddd;border-radius:4px;padding:6px 8px}
.testimonial h2{font-size:26px;margin-bottom:6px}
.testimonial p{font-size:11px;line-height:16px;text-align:justify}
.testimonial .quote{font-family:Georgia,serif;font-weight:700;font-size:16px;line-height:10px}
.client{position:absolute;right:24px;bottom:10px;font-size:11px;font-weight:700;text-decoration:underline;color:var(--ink)}
.client-quote{position:absolute;right:8px;bottom:2px;font-family:Georgia,serif;font-weight:700;font-size:16px}
.site-footer{left:0;top:1092px;width:1200px;height:34px;background:linear-gradient(var(--nav-red),var(--nav-red-dark));border-top:1px solid #900;color:var(--white);font-size:11px;text-align:center;line-height:34px}
</style>
</head>
<body>
<header class="site-header abs">
  <div class="brand abs"><span class="brand-mark"></span><span class="brand-name">Harbourline Realty</span></div>
  <div class="phone abs">
    <div class="phone-icon"><svg width="26" height="22" viewBox="0 0 26 22"><path d="M2 7 Q13 -1 24 7 L22 10 L18 8 L18 5 Q13 3 8 5 L8 8 L4 10 Z" fill="#222"/><rect x="5" y="11" width="16" height="10" rx="2" fill="#222"/><circle cx="13" cy="16" r="3" fill="#ddd"/></svg></div>
    <span class="phone-number">123 456 789</span>
  </div>
</header>
<nav class="main-nav abs">
  <ul class="nav-list">
    <li class="active">Home</li><li>Building</li><li>Buying</li><li>Selling</li><li>Moving</li><li>About Us</li><li>Contact Us</li>
  </ul>
  <div class="search">Search....<svg width="22" height="16" viewBox="0 0 22 16"><circle cx="8" cy="7" r="5" stroke="#111" stroke-width="2" fill="none"/><path d="M12 10 L19 15" stroke="#111" stroke-width="3"/></svg></div>
</nav>
<section class="feature-band abs"></section>
<div class="slide-arrow abs" style="left:88px">«</div>
<div class="slide-arrow abs" style="left:1058px">»</div>
<div class="slide-frame abs"><div class="slide-photo" role="img" aria-label="Featured property: two-storey stone and render family home with garage and front garden, with the sales consultant standing beside it"></div></div>
<div class="captions abs"><span>Dummy Text</span><span class="sep">|</span><span>Dummy Text</span><span class="sep">|</span><span>Dummy Text</span><span class="sep">|</span><span>Dummy Text</span><span class="sep">|</span><span>Dummy Text</span><span class="sep">|</span><span>Dummy Text</span></div>

<h2 class="about-title abs">Who We Are?</h2>
<div class="about-text abs">
  <p>Lorem Ipsum is simply dummy text of the printing and typesetting industry. Lorem Ipsum has been the industry's standard dummy text ever since the 1500s, when an unknown printer took a galley of type and scrambled it to make a type specimen book. It has survived not only five centuries, but also the leap into electronic typesetting, remaining essentially unchanged.</p>
  <p>It was popularised in the 1960s with the release of Typeline sheets containing Lorem Ipsum passages, and more recently with desktop publishing software like Pagecraft Studio including versions of Lorem Ipsum It has survived not only five centuries, but also the leap into electronic typesetting.</p>
</div>
<div class="agent-photo abs"><div role="img" aria-label="Portrait of the sales consultant in company uniform"></div></div>
<p class="about-more abs">It was popularised in the 1960s with the release of Typeline sheets containing Lorem Ipsum passages, and more recently with desktop publishing software like Pagecraft Studio including versions of Lorem Ipsum It has survived not only five centuries, but also the leap into electronic typesetting</p>

<h2 class="props-title abs">Properties For Sale</h2>
<div class="props-box abs"></div>
<svg class="prop-arrow abs" style="left:180px" width="30" height="34" viewBox="0 0 30 34"><path d="M26 2 L6 17 L26 32 L20 17 Z" fill="#2a2aa8"/></svg>
<svg class="prop-arrow abs" style="left:726px" width="30" height="34" viewBox="0 0 30 34"><path d="M4 2 L24 17 L4 32 L10 17 Z" fill="#2a2aa8"/></svg>
<div class="prop-thumb abs" style="left:222px;background:linear-gradient(#9cc3e8,#9b5a44 55%,#6d8f45)" role="img" aria-label="Brick family home for sale"></div>
<div class="prop-thumb abs" style="left:345px;background:linear-gradient(#b9cde0,#8a6a54 55%,#5f8a3e)" role="img" aria-label="Stone and brick house for sale"></div>
<div class="prop-thumb abs" style="left:468px;background:linear-gradient(#e8d88a,#c9a94a 60%,#8a7a5a)" role="img" aria-label="House with yellow timber deck for sale"></div>
<div class="prop-thumb abs" style="left:590px;background:linear-gradient(#a9c6e6,#6a6256 55%,#5d7f3d)" role="img" aria-label="Two-storey stone home for sale"></div>

<h2 class="news-title abs">News</h2>
<div class="news-item abs" style="top:664px">
  <div class="news-thumb"><div style="background:linear-gradient(#f1e9c8,#b58a52)" role="img" aria-label="Modern kitchen interior"></div></div>
  <div class="news-body"><div class="news-date">04/10/2011</div>Lorem Ipsum is simply dummy text of the printing and typesetting industry.</div>
  <span class="read-more">Read More</span>
</div>
<div class="news-item abs" style="top:761px;border-bottom:none">
  <div class="news-thumb"><div style="background:linear-gradient(#eef1f3,#9aa6ad)" role="img" aria-label="Agents meeting clients in an office"></div></div>
  <div class="news-body"><div class="news-date">04/10/2011</div>Lorem Ipsum is simply dummy text of the printing and typesetting industry.</div>
  <span class="read-more">Read More</span>
</div>

<aside class="testimonial abs">
  <h2>Testimonial</h2>
  <p><span class="quote">“</span> Lorem Ipsum is simply dummy text of the printing and typesetting industry. Lorem Ipsum has been the industry's standard dummy text ever since the 1500s, when an unknown printer took a galley of type and scrambled it to make a type specimen book. It has survived not only five centuries.</p>
  <span class="client">Happy Client</span><span class="client-quote">”</span>
</aside>

<footer class="site-footer abs">Copyright © 2003-2011 Harbourline Realty. All Rights Reserved</footer>
</body>
</html>
```